Pale Lantern Double Sided Flyer Design

We need a double sided flyer (1/3 of an A4 which is 99mm x 210mm) developed for our Newcastle(NSW) tour. This flyer will be placed in tourist information centres and hotels. We want it to direct people to our website or be able to make bookings over the phone.

About Us:-
We are a city walking tour company that runs tours day or night. We run both day and night and will incorporate real history / real Pale lantern. Some of the stories will be quite serious i.e.- there are infamous murders from 100 years ago, baffling court cases, even a bit of poetry written by murderers, suicides, love triangles, you name it. We will be telling the historical stories that tourists will not hear from any other tour provider. A bit of darkness, a bit of mystery and a bit of history theme.

We do no go for scares and let the very real stories deliver the entertainment for our guests. Our customers enjoy our tours, but it isn't light fun and frivolity. Our stories are being carefully crafted and are packed with unexpected twists, turns; revelations whilst remaining all 100% true. We deliver deep, rich, engaging stories.

Here are a few samples of quotes from the characters in our stories that may give you an idea of the kind of history we will cover:-

"There were bits of spines, bits of skulls, [and] finger bones spilled out all over the streets - I ended up filling three boxes. Children were playing with them for weeks”

"I had a close shave last night and now I want a close haircut.”

“She's a beautiful child', isn't she? She's the cause of all the trouble.”

“I did it because she would not come home with me.”

"I have killed my wife. I’m glad she’s dead.”

"Stand aside or I'll put a bullet through both of you."

“You villain, I'll teach you to take away my character."

“You’re not dead yet, you bastard!”

Our website, booking form and contact details can be viewed at www.palelantern.com.au

Target Market(s)

Tourists

Industry/Entity Type

Tour

Colors

Designer to choose colors to be used in the design.

Requirements
Must have
• Vertical orientation please.
• Please also include a reference to a discount offer of 25% using the promo code "WICK".
Nice to have
• FRONT FLYER INFORMATION
• - Pale Lantern Logo
• - "I have killed my wife; I'm glad she's dead."
• - Harbourside Hidden Lanes Walk
• - 25% Discount Offer Codeword WICK
• - web address at the base; www.palelantern.com.au
• BACK FLYER INFORMATION
• - "She's a beautiful child', isn't she? She's the cause of all the trouble.
• - Pale Lantern Logo at the base along with the web address www.palelantern.com.au
• - Blurb:- Pale lantern brings back Newcastle's hidden past, the forgotten past, the dark past that may not want to be remembered.
• Real stories from the streets around you. Discover the histories you won't hear anywhere else. The forgotten stories of yesteryear finally get a chance to be told. Through you they get to live again.
Should not have
• GENERAL
• Please do not include the phone number, email address or social media icons. We want to drive online bookings.

```html
<!DOCTYPE html>
<html lang="en">
<head>
<meta charset="utf-8">
<title>Pale Lantern – Harbourside Hidden Lanes Walk Flyer</title>
<link rel="stylesheet" href="https://fonts.googleapis.com/css2?family=Ubuntu:ital,wght@0,400;0,500;0,700;1,400;1,500;1,700&display=swap">
<style>
  :root {
    --ink: #070707;
    --red: #e4282f;
    --white: #ffffff;
    --backdrop: #e6e6e6;
    --stone-light: #d99a4e;
    --stone-mid: #8a4a1c;
    --stone-dark: #2a1206;
  }
  * { box-sizing: border-box; margin: 0; padding: 0; }
  html, body { width: 1200px; height: 1200px; overflow: hidden; }
  body {
    background: var(--backdrop);
    font-family: "Ubuntu", sans-serif;
    position: relative;
  }
  .flyer {
    position: absolute;
    top: 50px;
    width: 518px;
    height: 1100px;
    background: var(--ink);
    color: var(--white);
    overflow: hidden;
  }
  .flyer--back { left: 54px; }
  .flyer--front { left: 628px; }

  .tour-title {
    position: absolute;
    left: 0; right: 0;
    text-align: center;
    color: var(--red);
    font-weight: 500;
    text-transform: uppercase;
    line-height: 1.08;
  }
  .flyer--back .tour-title { top: 26px; font-size: 36px; }
  .flyer--front .tour-title { top: 118px; font-size: 41px; }

  .blurb {
    position: absolute;
    top: 166px; left: 10px; right: 10px;
    text-align: center;
    font-style: italic;
    font-weight: 700;
    font-size: 19.5px;
    line-height: 1.26;
  }

  .photo {
    position: absolute;
    left: 0; right: 0;
    background:
      radial-gradient(ellipse at 45% 60%, var(--stone-light) 0%, var(--stone-mid) 45%, transparent 80%),
      linear-gradient(180deg, var(--ink) 0%, var(--stone-dark) 30%, var(--stone-mid) 75%, var(--stone-dark) 100%);
  }
  .flyer--back .photo { top: 345px; height: 403px; }
  .flyer--front .photo { top: 268px; height: 308px; }

  .band {
    position: absolute;
    left: 0; right: 0;
    background: var(--red);
    display: flex;
    align-items: center;
    justify-content: center;
    text-align: center;
  }
  .quote-band { top: 748px; height: 102px; font-style: italic; font-size: 22px; line-height: 1.25; padding: 0 40px; }
  .offer-band { top: 576px; height: 80px; font-style: italic; font-weight: 700; font-size: 19px; }
  .url-band { top: 1052px; height: 48px; font-size: 19px; letter-spacing: 0.3px; }
  .flyer--front .url-band { top: 1054px; height: 46px; font-size: 15px; }

  .quote-line {
    position: absolute;
    top: 930px; left: 0; right: 0;
    text-align: center;
    font-style: italic;
    font-size: 16px;
  }

  .brand {
    position: absolute;
    left: 0; right: 0;
    display: flex;
    align-items: center;
    justify-content: center;
    gap: 10px;
    font-weight: 500;
    text-transform: uppercase;
    letter-spacing: 1px;
    color: var(--white);
  }
  .brand-dot {
    width: 22px; height: 22px;
    border: 3px solid var(--white);
    border-radius: 50%;
  }
  .flyer--back .brand { top: 988px; font-size: 22px; }
  .flyer--front .brand { top: 54px; font-size: 24px; }
</style>
</head>
<body>

<section class="flyer flyer--back" aria-label="Flyer back side">
  <h1 class="tour-title">Harbourside<br>Hidden Lanes<br>Walk</h1>
  <p class="blurb">Pale lantern brings back Newcastle's hidden past, the forgotten past, the dark past that may not want to be remembered.<br>Real stories from the streets around you. Discover the histories you won't hear anywhere else. The forgotten stories of yesteryear finally get a chance to be told. Through you they get to live again.</p>
  <div class="photo" role="img" aria-label="Old sandstone courthouse lit amber at night against a black sky"></div>
  <p class="band quote-band">"She's a beautiful child, isn't she? She's the cause of all the trouble"</p>
  <div class="brand"><span class="brand-dot"></span><span>Pale Lantern</span></div>
  <p class="band url-band">www.palelantern.com.au</p>
</section>

<section class="flyer flyer--front" aria-label="Flyer front side">
  <div class="brand"><span class="brand-dot"></span><span>Pale Lantern</span></div>
  <h1 class="tour-title">Harbourside<br>Hidden Lanes<br>Walk</h1>
  <div class="photo" role="img" aria-label="Old sandstone courthouse lit amber at night against a black sky"></div>
  <p class="band offer-band">25% Discount Offer Codeword WICK</p>
  <p class="quote-line">"I have killed my wife; I'm glad she's dead."</p>
  <p class="band url-band">www.palelantern.com.au</p>
</section>

</body>
</html>
```